Exciting, Bold and Modern Landscaping & Turf care company business card

Hello, I own a lawn and landscaping company in Virginia, USA. We would like to design a bold, dynamic, modern business card that really makes us stand out. I tire of all green business cards with crappy, cartoonish clipart grass on them. It needs to be two sided, on one side i need to highlight our turf care division called "Promised Brighter Meadow" We maintain grass, fertilize it, weed control, etc.. We have a green thumbed gopher as our logo that i will attach. I am looking for something, clean and neat but out of the box in style. Im open to all ideas, and would like different options for them. On the other side, i want to highlight our landscaping division "Quiet Harbor Landscaping" In this division we design and install landscapes. Feel free to visit our website for more info or email me with ANY questions. Our busines cards in the past have highlighted our different services, but i don't want to this time. By the time I hand out a business card we are usually already estimating a project and they know what services we offer. I do want them to look at my card and say "wow thats pretty cool" and for them to think "These guys are something different, not just your standard dirt diggers" The logo doesnt have to be on both sides, but it needs to be on the turf care side. Our phone number and website should also be on at least on side, but need not be on both. The phone number is (555)618-4072 as well as the web address as www.MossbrookYardWorks.example. I like for the web address to have caps like that becasue it makes the long address much easier to read. I would like it in full color, printing costs are not my major concern. I also love rounded corners or interesting die cut designs as well, so feel free to wow me. Whether it be a clean white background with a bold photo to an all black card with a gray logo except for his green thumb with silver foil lettering to anything in between, lets go for it. That bieng said i dont want anything cartoonish, we are still a professional service and i want that to come through. THANKS!
Updates
Project Deadline Extended
Reason: changed project to a committed payment. I would like designers to re-evaluate their interest now and give them extra time to submit designs. Thank you.
we have changed our status to a commited payment to entice more submissions. thank you all for your hard work!
Industry/Entity Type
Professional Service
Look and feel
Each slider illustrates characteristics of the customer's brand and the style your logo design should communicate.

```html
<!DOCTYPE html>
<html lang="en">
<head>
<meta charset="utf-8">
<title>Quiet Harbor Landscaping – Business Cards</title>
<link href="https://fonts.googleapis.com/css2?family=Cabin:wght@400;500;600&display=swap" rel="stylesheet">
<style>
  :root {
    --stage: #5a5a5a;
    --card: #050505;
    --white: #ffffff;
    --lime: #a8d13c;
    --turf: #2f9a4c;
    --icon: #c8a98a;
    --field-top: #1f3a17;
    --field-mid: #3f6a1e;
    --field-low: #9fd03a;
    --mascot-a: #6f6c6a;
    --mascot-b: #3c3a39;
  }
  * { box-sizing: border-box; margin: 0; padding: 0; }
  html, body { width: 1200px; height: 949px; overflow: hidden; }
  body {
    background: var(--stage);
    font-family: "Cabin", "Gill Sans", sans-serif;
    display: flex;
    flex-direction: column;
    align-items: center;
    justify-content: center;
    gap: 56px;
  }
  .card {
    position: relative;
    width: 630px;
    height: 360px;
    background: var(--card);
    border-radius: 24px;
    overflow: hidden;
    color: var(--white);
  }
  .contact {
    position: absolute;
    right: 40px;
    top: 44px;
    text-align: right;
  }
  .division-name {
    font-weight: 600;
    font-size: 25px;
    letter-spacing: 0.2px;
  }
  .landscape .division-name { color: var(--lime); }
  .turf .division-name { color: var(--turf); }
  .address {
    font-size: 17px;
    line-height: 1.25;
    margin-top: 4px;
  }
  .phone {
    display: inline-flex;
    align-items: center;
    gap: 10px;
    font-size: 26px;
    margin-top: 8px;
  }
  .phone svg { width: 26px; height: 26px; }
  .field-photo {
    position: absolute;
    left: 0;
    bottom: 0;
    width: 68%;
    height: 112px;
    background: linear-gradient(180deg, var(--field-top) 0%, var(--field-mid) 42%, var(--field-low) 100%);
    -webkit-mask-image: linear-gradient(90deg, #000 70%, transparent 100%);
    mask-image: linear-gradient(90deg, #000 70%, transparent 100%);
  }
  .mascot {
    position: absolute;
    left: 0;
    bottom: 0;
    width: 300px;
    height: 330px;
    background: radial-gradient(ellipse at 45% 50%, var(--mascot-a) 0%, var(--mascot-b) 55%, transparent 78%);
  }
  .grass-strip {
    position: absolute;
    left: 0;
    bottom: 0;
    width: 320px;
    height: 16px;
    background: linear-gradient(90deg, #3f8a2a, #5fae34 70%, transparent);
  }
  .website {
    position: absolute;
    right: 40px;
    bottom: 40px;
    font-size: 15px;
  }
  .website .site-name { color: var(--turf); }
</style>
</head>
<body>

  <section class="card landscape">
    <div class="contact">
      <p class="division-name">"Quiet Harbor Landscaping"</p>
      <p class="address">4810-202 Alder Ln. PMB 118<br>Fernwood Bay, VA 20999</p>
      <p class="phone">(555)618-4072
        <svg viewBox="0 0 26 26" aria-hidden="true">
          <circle cx="13" cy="13" r="11.5" fill="none" stroke="var(--icon)" stroke-width="1.6"/>
          <path d="M9 7.5c-1 .6-1.6 1.7-1.2 3.2.9 3.2 3.4 6.3 6.5 7.7 1.3.6 2.6.2 3.3-.7l-2.2-2.1-1.5.8c-1.4-.8-2.6-2.2-3.3-3.7l1.2-1.2L10.6 8z" fill="var(--icon)"/>
        </svg>
      </p>
    </div>
    <div class="field-photo" role="img" aria-label="Photo of a green striped lawn with a dark tree line behind it"></div>
  </section>

  <section class="card turf">
    <div class="mascot" role="img" aria-label="Turf care mascot illustration giving a green thumbs up"></div>
    <div class="grass-strip" role="img" aria-label="Grass tuft beneath the mascot"></div>
    <div class="contact">
      <p class="division-name">"Promised Brighter Meadow"</p>
      <p class="phone">(555)618-4072
        <svg viewBox="0 0 26 26" aria-hidden="true">
          <circle cx="13" cy="13" r="11.5" fill="none" stroke="var(--icon)" stroke-width="1.6"/>
          <path d="M9 7.5c-1 .6-1.6 1.7-1.2 3.2.9 3.2 3.4 6.3 6.5 7.7 1.3.6 2.6.2 3.3-.7l-2.2-2.1-1.5.8c-1.4-.8-2.6-2.2-3.3-3.7l1.2-1.2L10.6 8z" fill="var(--icon)"/>
        </svg>
      </p>
    </div>
    <p class="website">www.<span class="site-name">MossbrookYardWorks</span>.example</p>
  </section>

</body>
</html>
```